Personal Injury Lawyer Billboard

I would like a design created featuring the image of the lawyer centered in the middle of the design.
To the left of the lawyer's image it should read "INJURED?"
To the right of the lawyer's image, it should read "CALL BRUNO!"
Under Call Bruno, include the phone number 318-555-0187.
At the bottom of the design include the lawyers information "Bruno Pemberly Accident & Injury Lawyers"
PLEASE REMOVED THE BACKGROUND IMAGERY OF THE PHOTO SUBMITTED. Also, the colors for this design should match the colors shown in the logo (navy, white and relective soft gold). Please use those color combinations in ways that best stand out.

```html
<!DOCTYPE html>
<html lang="en">
<head>
<meta charset="utf-8">
<title>Bruno Pemberly Accident &amp; Injury Lawyers – Billboard</title>
<link rel="stylesheet" href="https://fonts.googleapis.com/css2?family=Krona+One&family=Oswald:wght@500;600&display=swap">
<style>
  :root {
    --backdrop: #c0c0c0;
    --navy: #0b1c45;
    --gold: #d2b044;
    --gold-light: #ecd27a;
    --gold-dark: #b8922c;
    --white: #ffffff;
  }
  * { box-sizing: border-box; margin: 0; padding: 0; }
  html, body {
    width: 1200px; height: 522px; overflow: hidden;
    background: var(--backdrop);
  }
  .billboard {
    position: absolute; left: 86px; top: 110px;
    width: 1030px; height: 301px;
    box-shadow: 0 4px 14px rgba(0,0,0,0.25);
  }
  .billboard__main {
    position: absolute; left: 0; top: 0; width: 100%; height: 212px;
    background: var(--navy);
  }
  .billboard__band {
    position: absolute; left: 0; top: 212px; width: 100%; height: 89px;
    background: var(--gold);
    display: flex; align-items: center; justify-content: center;
    padding-bottom: 10px;
    font-family: "Krona One", sans-serif; font-size: 19px;
    white-space: nowrap;
  }
  .band__name { color: var(--navy); }
  .band__practice { color: var(--white); margin-left: 14px; }

  .gold-text {
    background: linear-gradient(180deg, var(--gold-light) 0%, var(--gold) 50%, var(--gold-dark) 100%);
    -webkit-background-clip: text; background-clip: text;
    color: transparent;
  }
  .headline-question {
    position: absolute; left: 22px; top: 24px;
    font-family: "Krona One", sans-serif; font-size: 52px; font-weight: 400;
    line-height: 1; white-space: nowrap;
  }
  .firm-name {
    position: absolute; left: 26px; top: 96px; width: 322px;
    font-family: "Oswald", sans-serif; font-weight: 500; color: var(--white);
    text-align: center; white-space: nowrap;
  }
  .firm-name__primary { display: block; font-size: 40px; line-height: 1.1; }
  .firm-name__secondary { display: block; font-size: 23px; line-height: 1.4; margin-top: 6px; }
  .lawyer-photo {
    position: absolute; left: 423px; top: 6px; width: 210px; height: 206px;
  }
  .call-to-action {
    position: absolute; left: 650px; top: 36px; width: 370px;
    font-family: "Oswald", sans-serif; white-space: nowrap;
  }
  .call-to-action__line {
    font-size: 64px; font-weight: 600; line-height: 1;
  }
  .call-to-action__phone {
    margin-top: 12px;
    color: var(--white); font-size: 60px; font-weight: 500; line-height: 1;
  }
</style>
</head>
<body>
  <section class="billboard">
    <div class="billboard__main">
      <h1 class="headline-question gold-text">INJURED?</h1>
      <p class="firm-name">
        <span class="firm-name__primary">BRUNO PEMBERLY</span>
        <span class="firm-name__secondary">ACCIDENT &amp; INJURY LAWYERS</span>
      </p>

      <svg class="lawyer-photo" role="img" aria-label="Portrait of attorney Bruno in a navy suit and green tie, smiling with a raised fist" viewBox="0 0 210 206" preserveAspectRatio="none">
        <defs>
          <linearGradient id="portraitTone" x1="0" y1="0" x2="0" y2="1">
            <stop offset="0" stop-color="#0b1c45"/>
            <stop offset="0.45" stop-color="#2a2f4a"/>
            <stop offset="1" stop-color="#17234f"/>
          </linearGradient>
        </defs>
        <rect width="210" height="206" fill="url(#portraitTone)"/>
      </svg>

      <div class="call-to-action">
        <p class="call-to-action__line gold-text">CALL BRUNO!</p>
        <p class="call-to-action__phone">318-555-0187</p>
      </div>
    </div>

    <div class="billboard__band">
      <span class="band__name">BRUNO PEMBERLY</span>
      <span class="band__practice">ACCIDENT &amp; INJURY LAWYERS</span>
    </div>
  </section>
</body>
</html>
```